Label Fjordulin
Zielgruppe
Hunde- und Katzenhalter von Jung bis Alt
Aufgabenstellung
Es soll ein Flaschenetikett für folgendes Produkt entworfen werden:
Lachsöl aus Norwegen für Hunde und Katzen. Es handelt sich um ein Premium-Produkt. Der Name "Fjordulin" sowie einige weitere Etikettendetails wie Größe, Deklaration etc. liegen fest. Die Flaschenfarbe ist braun. Ansonsten ist die Gestaltung frei. Ein Musteretikett des Herstellers kann geliefert werden.
Das Ur-Produkt ist Krevanix-Lachsöl (www.krevanix.no), welches von uns als Privat-Label-Produkt erworben wird.

```html
<!DOCTYPE html>
<html lang="de">
<head>
<meta charset="utf-8">
<title>Fjordulin – Flaschenetikett</title>
<link href="https://fonts.googleapis.com/css2?family=Arimo:wght@400;700&display=swap" rel="stylesheet">
<style>
  :root {
    --page: #ffffff;
    --label-orange: #ff9933;
    --frame-cream: #fff6cc;
    --brand-red: #b81c0c;
    --text-red: #c0260e;
    --panel-white: #ffffff;
    --ink: #1a1a1a;
    --date-field: #ffffcc;
    --emblem-light: #fffbe8;
    --emblem-gold: #f2c23a;
    --emblem-rim: #a31a0a;
  }
  html, body {
    margin: 0;
    padding: 0;
    width: 1031px;
    height: 1200px;
    overflow: hidden;
    background: var(--page);
  }
  .label {
    position: relative;
    width: 1031px;
    height: 1200px;
    font-family: "Arimo", Arial, sans-serif;
  }
  .label__sheet {
    position: absolute;
    left: 40px; top: 30px;
    width: 960px; height: 1140px;
    background: var(--label-orange);
  }
  .label__frame {
    position: absolute;
    left: 84px; top: 70px;
    width: 862px; height: 1040px;
    border: 5px solid var(--frame-cream);
    border-radius: 50px;
  }
  .label__emblem {
    position: absolute;
    left: 336px; top: 120px;
    width: 360px; height: 360px;
  }
  .label__brand {
    position: absolute;
    left: 0; width: 1031px;
    top: 512px;
    margin: 0;
    text-align: center;
    font-size: 118px;
    font-weight: 700;
    line-height: 1;
    color: var(--brand-red);
  }
  .label__product {
    position: absolute;
    left: 0; width: 1031px;
    top: 682px;
    margin: 0;
    text-align: center;
    font-size: 40px;
    font-weight: 400;
    line-height: 60px;
    color: var(--text-red);
  }
  .label__benefits {
    position: absolute;
    left: 176px; top: 820px;
    width: 716px; height: 148px;
    box-sizing: border-box;
    padding-top: 12px;
    background: var(--panel-white);
    border-radius: 18px;
    text-align: center;
    font-size: 30px;
    line-height: 40px;
    color: var(--text-red);
    margin: 0;
  }
  .label__expiry {
    position: absolute;
    left: 136px; top: 990px;
    font-size: 35px;
    color: var(--ink);
    margin: 0;
  }
  .label__expiry-field {
    position: absolute;
    left: 136px; top: 1054px;
    width: 204px; height: 48px;
    background: var(--date-field);
  }
  .label__batch {
    position: absolute;
    left: 540px; top: 986px;
    width: 400px;
    text-align: center;
    font-size: 38px;
    line-height: 46px;
    color: var(--ink);
    margin: 0;
  }
</style>
</head>
<body>
  <main class="label">
    <div class="label__sheet"></div>
    <div class="label__frame"></div>

    <svg class="label__emblem" viewBox="0 0 360 360" role="img" aria-label="Rundes Emblem mit Hund und Katze">
      <defs>
        <radialGradient id="emblemFill" cx="50%" cy="50%" r="50%">
          <stop offset="0%" stop-color="var(--emblem-light)"/>
          <stop offset="72%" stop-color="var(--emblem-light)"/>
          <stop offset="100%" stop-color="var(--emblem-gold)"/>
        </radialGradient>
      </defs>
      <circle cx="180" cy="180" r="176" fill="url(#emblemFill)" stroke="var(--emblem-rim)" stroke-width="4"/>
    </svg>

    <h1 class="label__brand">Fjordulin</h1>

    <p class="label__product">Original norwegisches Lachsöl<br>für Hunde und Katzen</p>

    <p class="label__benefits">Mit wichtigen Omega 3 und 6 Fettsäuren<br>für ein glänzendes Fell, gegen Ekzeme<br>und für ein langes Leben.</p>

    <p class="label__expiry">Haltbar bis</p>
    <div class="label__expiry-field"></div>

    <p class="label__batch">Chargennummer<br>PO324-H83</p>
  </main>
</body>
</html>
```